Customer Dashboard Design for Email Security SaaS

Mailbrook is a commercial email spam filter offered as a SaaS product, built and operated by a small German hosting provider. It protects business email accounts against spam, phishing, scam, and viruses using a multilayer filtering pipeline that combines traditional spam detection with AI-powered classification. The product runs entirely on German infrastructure, ensuring data sovereignty for European customers.

We need a complete redesign of the customer-facing dashboard. This is the web application where paying customers manage their email filtering: view their mail log, check quarantined emails, manage allow/blocklists, configure their settings, and handle their subscription. It is the primary touchpoint between Mailbrook and its customers.

Our customers are system administrators, IT managers at small-to-medium businesses, and operators of small hosting providers. They are technically competent but not designers. They expect professional, efficient tools that respect their time. They typically manage 10–500 email accounts and check the dashboard a few times per week, with heavier use during spam incidents.

We have attached the current mockups which really need to be replaced with something good looking.

Target Market(s)

System administrators, IT managers at small-to-medium businesses, and operators of small hosting providers.

Industry/Entity Type

SaaS

Number of Pages Required

5+ page

```html
<!DOCTYPE html>
<html lang="de">
<head>
<meta charset="utf-8">
<title>Mailbrook – Übersicht</title>
<link href="https://fonts.googleapis.com/css2?family=Poppins:wght@400;500;600&family=Oswald:wght@500&display=swap" rel="stylesheet">
<style>
:root{
  --bg:#0a0e18;
  --header:#0c1a3b;
  --sidebar:#0f1d45;
  --card:#111827;
  --card-border:#1e2940;
  --green:#059669;
  --green-bar:#0f473b;
  --text:#ffffff;
  --muted:#6b7280;
  --line:#243044;
  --spam:#ef4444;
  --spam-bg:#2a1620;
  --phish:#f97316;
  --phish-bg:#2a1c18;
  --virus:#dc2626;
  --virus-bg:#241724;
  --news:#3b6cf0;
  --news-bg:#16213f;
  --quar:#d4b800;
  --temp:#8a8f98;
}
*{box-sizing:border-box;margin:0;padding:0}
html,body{width:1200px;height:904px;overflow:hidden}
body{background:var(--bg);font-family:"Poppins",sans-serif;color:var(--text);position:relative}
.header{position:absolute;left:0;top:0;width:1200px;height:57px;background:var(--header)}
.brand{position:absolute;left:8px;top:10px;display:flex;align-items:center;gap:11px}
.brand-mark{width:37px;height:37px;border-radius:8px;background:var(--green)}
.brand-name{font-size:18px;font-weight:500}
.search{position:absolute;left:587px;top:12px;width:356px;height:33px;border:1px solid #27345a;border-radius:17px;background:#0a1430;display:flex;align-items:center;padding-left:14px;font-size:10px;color:#d1d5db}
.search-btn{position:absolute;right:2px;top:2px;width:27px;height:27px;border-radius:50%;background:var(--green);display:flex;align-items:center;justify-content:center}
.round-btn{position:absolute;top:15px;width:30px;height:30px;border-radius:50%;background:var(--green);display:flex;align-items:center;justify-content:center}
.avatar{position:absolute;left:1055px;top:13px;width:32px;height:32px;border-radius:50%;background:linear-gradient(135deg,#8a7a6a,#3d4a5a)}
.user{position:absolute;left:1097px;top:15px;line-height:1.3}
.user-role{font-size:10px;font-weight:500}
.user-name{font-size:11px;font-weight:600}
.sidebar{position:absolute;left:0;top:57px;width:227px;height:847px;background:var(--sidebar)}
.nav-item{position:absolute;left:8px;width:208px;height:37px;border:1px solid #2a3760;border-radius:4px;display:flex;align-items:center;padding-left:2px;gap:11px;font-size:13px}
.nav-item.active{background:var(--green);border-color:var(--green);font-weight:600}
.nav-icon{width:30px;height:30px;border-radius:4px;background:var(--green);display:flex;align-items:center;justify-content:center}
.nav-item.active .nav-icon{background:#fff}
.title{position:absolute;left:268px;top:75px;font-size:25px;font-weight:600}
.subtitle{position:absolute;left:268px;top:114px;font-size:14px}
.stat{position:absolute;top:158px;width:290px;height:164px;background:var(--card);border:1px solid var(--card-border);border-radius:10px}
.stat-icon{position:absolute;left:10px;top:11px;width:47px;height:47px;border-radius:6px;background:var(--green);display:flex;align-items:center;justify-content:center}
.stat-label{position:absolute;left:10px;top:70px;font-size:15px}
.stat-value{position:absolute;left:8px;top:93px;font-family:"Oswald",sans-serif;font-size:28px;font-weight:500}
.stat-sub{position:absolute;left:10px;top:131px;font-size:12.5px}
.section-title{position:absolute;left:268px;top:362px;font-size:24px;font-weight:600}
.chart-panel{position:absolute;left:268px;top:412px;width:897px;height:451px;background:var(--card);border:1px solid var(--card-border);border-radius:10px}
.pill{position:absolute;top:446px;height:27px;border-radius:14px;font-size:12px;display:flex;align-items:center;justify-content:center}
.bars{position:absolute;left:299px;top:500px;width:838px;height:214px}
.bar{position:absolute;bottom:0;width:111px;background:var(--green-bar);border-radius:3px 3px 0 0}
.bar-label{position:absolute;top:721px;width:111px;text-align:center;font-size:12px;color:var(--muted)}
.axis{position:absolute;left:297px;top:749px;width:842px;height:1px;background:var(--line)}
.legend{position:absolute;top:772px;display:flex;align-items:center;gap:6px;font-size:12px}
.swatch{width:10px;height:10px;border-radius:1px}
.table-link{position:absolute;left:297px;top:808px;font-size:14px}
</style>
</head>
<body>
<header class="header">
  <div class="brand"><div class="brand-mark"></div><span class="brand-name">Mailbrook</span></div>
  <div class="search">Search...
    <div class="search-btn"><svg width="14" height="14" viewBox="0 0 24 24" fill="none" stroke="#fff" stroke-width="2.5"><circle cx="10" cy="10" r="7"/><path d="M15 15l6 6"/></svg></div>
  </div>
  <div class="round-btn" style="left:970px"><svg width="14" height="14" viewBox="0 0 24 24" fill="none" stroke="#fff" stroke-width="2"><path d="M3 10l9-6 9 6v10H3z"/><path d="M3 10l9 6 9-6"/></svg></div>
  <div class="round-btn" style="left:1010px"><svg width="14" height="14" viewBox="0 0 24 24" fill="none" stroke="#fff" stroke-width="2"><path d="M6 17V11a6 6 0 0112 0v6l2 2H4z"/><path d="M10 21h4"/></svg></div>
  <div class="avatar" role="img" aria-label="Profilfoto des Benutzers"></div>
  <div class="user"><div class="user-role">Super Admin</div><div class="user-name">Martin Keller</div></div>
</header>

<nav class="sidebar">
  <div class="nav-item active" style="top:14px"><span class="nav-icon"><svg width="16" height="16" viewBox="0 0 24 24" fill="none" stroke="#111" stroke-width="2"><path d="M3 11l9-7 9 7v10H3z"/><path d="M10 21v-6h4v6"/></svg></span>Übersicht</div>
  <div class="nav-item" style="top:59px"><span class="nav-icon"><svg width="16" height="16" viewBox="0 0 24 24" fill="none" stroke="#fff" stroke-width="2"><path d="M3 5h18M3 10h18M3 15h18M3 20h18"/></svg></span>Mail-Log</div>
  <div class="nav-item" style="top:103px"><span class="nav-icon"><svg width="16" height="16" viewBox="0 0 24 24" fill="none" stroke="#fff" stroke-width="2"><path d="M3 10l9-6 9 6v10H3z"/><path d="M3 10l9 6 9-6"/></svg></span>Postfächer</div>
  <div class="nav-item" style="top:148px"><span class="nav-icon"><svg width="16" height="16" viewBox="0 0 24 24" fill="none" stroke="#fff" stroke-width="2"><circle cx="8" cy="9" r="3"/><path d="M2 19c1-4 11-4 12 0M15 8h7M15 12h7M17 16h5"/></svg></span>Allowlist</div>
  <div class="nav-item" style="top:194px"><span class="nav-icon"><svg width="16" height="16" viewBox="0 0 24 24" fill="none" stroke="#fff" stroke-width="2"><circle cx="10" cy="8" r="4"/><path d="M3 20c1-5 11-5 12-2"/><circle cx="18" cy="18" r="3"/><path d="M16 20l4-4"/></svg></span>Blocklist</div>
  <div class="nav-item" style="top:241px"><span class="nav-icon"><svg width="16" height="16" viewBox="0 0 24 24" fill="none" stroke="#fff" stroke-width="2"><rect x="4" y="10" width="16" height="11" rx="1"/><path d="M8 10V7a4 4 0 018 0v3"/></svg></span>Quarantane</div>
  <div class="nav-item" style="top:288px"><span class="nav-icon"><svg width="16" height="16" viewBox="0 0 24 24" fill="none" stroke="#fff" stroke-width="2"><circle cx="12" cy="12" r="3"/><path d="M12 2l2 3 3-1 1 3 3 2-2 3 2 3-3 2-1 3-3-1-2 3-2-3-3 1-1-3-3-2 2-3-2-3 3-2 1-3 3 1z"/></svg></span>Einstellungen</div>
  <div class="nav-item" style="top:333px"><span class="nav-icon"><svg width="16" height="16" viewBox="0 0 24 24" fill="none" stroke="#fff" stroke-width="2"><rect x="3" y="4" width="18" height="12" rx="1"/><path d="M9 20h6M12 16v4M10 12h4M12 7v6"/></svg></span>Abrechnung</div>
</nav>

<h1 class="title">Guten Tag</h1>
<p class="subtitle">Seobachtungsmodus - Mails Werden Analysiert Aber Nicht Blockiert</p>

<div class="stat" style="left:268px">
  <div class="stat-icon"><svg width="24" height="24" viewBox="0 0 24 24" fill="none" stroke="#fff" stroke-width="2"><circle cx="12" cy="12" r="9"/><path d="M12 7v5l3 2"/></svg></div>
  <div class="stat-label">Letzte 24 Stunden</div>
  <div class="stat-value">85</div>
  <div class="stat-sub">O zugestellt, O abgefangen</div>
</div>
<div class="stat" style="left:572px">
  <div class="stat-icon"><svg width="24" height="24" viewBox="0 0 24 24" fill="none" stroke="#fff" stroke-width="2"><path d="M3 12V4h8l10 10-8 8z"/><circle cx="8" cy="8" r="1.5"/></svg></div>
  <div class="stat-label">7 TAGE</div>
  <div class="stat-value">34</div>
  <div class="stat-sub">0% zugestellt</div>
</div>
<div class="stat" style="left:875px">
  <div class="stat-icon"><svg width="24" height="24" viewBox="0 0 24 24" fill="none" stroke="#fff" stroke-width="2"><rect x="3" y="5" width="16" height="15" rx="2"/><path d="M3 10h16M8 3v4M14 3v4"/><circle cx="18" cy="18" r="4" fill="#059669"/><path d="M18 16v2l1 1"/></svg></div>
  <div class="stat-label">30 TAGE</div>
  <div class="stat-value">42</div>
  <div class="stat-sub">0% zugestellt</div>
</div>

<h2 class="section-title">Letzte 30 Tage</h2>
<section class="chart-panel"></section>

<span class="pill" style="left:299px;width:57px;background:var(--green);color:#fff">ALLE</span>
<span class="pill" style="left:366px;width:62px;background:var(--spam-bg);color:var(--spam)">SPAM</span>
<span class="pill" style="left:438px;width:85px;background:var(--phish-bg);color:var(--phish)">PHISHING</span>
<span class="pill" style="left:534px;width:63px;background:var(--virus-bg);color:var(--virus)">VIRUS</span>
<span class="pill" style="left:608px;width:106px;background:var(--news-bg);color:var(--news)">NEWSLETTER</span>
<span class="pill" style="left:924px;width:62px;background:var(--green);color:#fff">7 TAGE</span>
<span class="pill" style="left:994px;width:67px;background:#0a0e18;border:1px solid #2a3348">14 TAGE</span>
<span class="pill" style="left:1069px;width:69px;background:#0a0e18;border:1px solid #2a3348">30 TAGE</span>

<div class="bars">
  <div class="bar" style="left:0;height:150px"></div>
  <div class="bar" style="left:121px;height:103px"></div>
  <div class="bar" style="left:242px;height:95px"></div>
  <div class="bar" style="left:363px;height:86px"></div>
  <div class="bar" style="left:485px;height:129px"></div>
  <div class="bar" style="left:606px;height:152px"></div>
  <div class="bar" style="left:727px;height:192px"></div>
</div>
<span class="bar-label" style="left:299px">4/8</span>
<span class="bar-label" style="left:420px">4/9</span>
<span class="bar-label" style="left:541px">4/10</span>
<span class="bar-label" style="left:662px">4/11</span>
<span class="bar-label" style="left:784px">4/12</span>
<span class="bar-label" style="left:905px">4/13</span>
<span class="bar-label" style="left:1026px">4/14</span>
<div class="axis"></div>

<div class="legend" style="left:297px"><span class="swatch" style="background:var(--green)"></span>AKZEPTIERT</div>
<div class="legend" style="left:412px"><span class="swatch" style="background:var(--spam)"></span>ABGELEHNT</div>
<div class="legend" style="left:527px"><span class="swatch" style="background:var(--quar)"></span>QUARANTÄNE</div>
<div class="legend" style="left:653px"><span class="swatch" style="background:var(--temp)"></span>TEMPFAIL</div>

<div class="table-link">Datentabelle Anzeigen</div>
</body>
</html>
```